Medical equipment business looking for professional, unique business card

We need a business card design for a durable medical equipment company. We are small but would like our cards to express that we are much bigger. We focus on braces (back, knee, wrist, etc) but also do crutches, rollators, wheelchairs- basically medical equipment that gets you going and back in Action. Our colors are blue and green and our logo has an arrow and use of a "spine". We'd like to express professionalism while being unique.

Industry/Entity Type

Medical Equipment

Contact Information for Business Card

Professional feel but unique. Memorable.

Font styles to use
Serif
Sans Serif
Other font styles liked:
• verdana

Requirements
Must have
• card holders cell#, business phone#, fax#, email, website address, business address, logo
Nice to have
• use of medical/healthcare related descriptive words, items, look
Should not have
• the wrong colors or cartoon characters.

```html
<!DOCTYPE html>
<html lang="en">
<head>
<meta charset="utf-8">
<title>Stride DME – Business Card</title>
<link rel="stylesheet" href="https://fonts.googleapis.com/css2?family=Open+Sans:wght@400;600;700&display=swap">
<style>
  :root {
    --navy: #0b4468;
    --navy-deep: #0f3c63;
    --green: #8cc63f;
    --text-grey: #444a50;
    --paper: #ffffff;
    --backdrop: #e9ecef;
  }
  * { box-sizing: border-box; margin: 0; padding: 0; }
  html, body {
    width: 1200px; height: 1000px; overflow: hidden;
    background: var(--backdrop);
    font-family: "Open Sans", Verdana, sans-serif;
  }
  .card {
    position: absolute; left: 266px; width: 666px; height: 396px;
    border-radius: 24px; overflow: hidden;
  }
  .card--front { top: 74px; background: var(--paper); }
  .card--back { top: 534px; background: var(--navy); }

  .wave { position: absolute; left: 0; top: 0; width: 666px; height: 396px; }

  .brand {
    position: absolute; display: flex; align-items: center; gap: 12px;
    font-weight: 600; white-space: nowrap;
  }
  .brand__dot { border-radius: 50%; background: var(--green); flex: none; }
  .card--front .brand { right: 48px; top: 38px; font-size: 46px; color: var(--navy-deep); }
  .card--front .brand__dot { width: 20px; height: 20px; }
  .card--back .brand { left: 50%; top: 128px; transform: translateX(-50%); font-size: 58px; color: var(--paper); }
  .card--back .brand__dot { width: 24px; height: 24px; }

  .holder { position: absolute; left: 33px; top: 178px; }
  .holder__name { font-size: 20px; font-weight: 700; color: var(--navy-deep); letter-spacing: 0.3px; }
  .holder__title { font-size: 16px; color: var(--green); margin-top: 2px; }

  .contact { position: absolute; left: 414px; top: 172px; color: var(--text-grey); font-size: 16px; line-height: 23px; }
  .contact__address { margin-bottom: 12px; }
  .contact__row { display: flex; align-items: center; gap: 8px; }
  .contact__icon { width: 14px; height: 14px; flex: none; }

  .web { position: absolute; color: var(--paper); }
  .card--front .web { left: 32px; bottom: 26px; font-size: 15px; letter-spacing: 0.3px; }
  .card--back .web { left: 0; right: 0; bottom: 32px; text-align: center; font-size: 16px; letter-spacing: 2.5px; }
</style>
</head>
<body>

<section class="card card--front">
  <svg class="wave" viewBox="0 0 666 396" aria-hidden="true">
    <path d="M0 330 C 110 300, 220 290, 330 330 S 560 390, 666 300 L 666 396 L 0 396 Z" fill="var(--navy)"/>
    <path d="M0 330 C 110 300, 220 290, 330 330 S 560 390, 666 300 L 666 306 C 560 380, 450 360, 330 322 S 110 296, 0 326 Z" fill="#ffffff"/>
    <path d="M74 306 C 180 296, 260 300, 340 320 S 560 380, 652 318 C 560 370, 440 350, 340 312 S 170 292, 74 306 Z" fill="var(--green)"/>
  </svg>

  <div class="brand"><span class="brand__dot"></span>Stride DME</div>

  <div class="holder">
    <div class="holder__name">DANA WHITFIELD</div>
    <div class="holder__title">Managing Director</div>
  </div>

  <div class="contact">
    <div class="contact__address">Post Office Box 4410372<br>Riverton, LA 70412</div>
    <div class="contact__row">
      <svg class="contact__icon" viewBox="0 0 14 14" aria-label="Mobile"><rect x="3.5" y="0.5" width="7" height="13" rx="1.5" fill="none" stroke="var(--green)" stroke-width="1.4"/></svg>
      + 000 000 0000 EXT 1</div>
    <div class="contact__row">
      <svg class="contact__icon" viewBox="0 0 14 14" aria-label="Phone"><path d="M1 5 Q7 0 13 5 L11 7 L9 5 L5 5 L3 7 Z" fill="var(--green)"/><rect x="2.5" y="7.5" width="9" height="5" rx="1" fill="var(--green)"/></svg>
      + 000 000 0000 EXT 1</div>
    <div class="contact__row">
      <svg class="contact__icon" viewBox="0 0 14 14" aria-label="Fax"><rect x="3.5" y="1" width="7" height="4" fill="var(--green)"/><rect x="1" y="5" width="12" height="6" rx="1" fill="var(--green)"/><rect x="3.5" y="9" width="7" height="4" fill="#fff" stroke="var(--green)" stroke-width="1"/></svg>
      + 000 000 0000 EXT 1</div>
    <div class="contact__row">
      <svg class="contact__icon" viewBox="0 0 14 14" aria-label="Email"><rect x="0.5" y="3" width="13" height="9" fill="var(--green)"/><path d="M0.5 3 L7 8 L13.5 3" fill="none" stroke="#fff" stroke-width="1"/></svg>
      info@StrideDME.com</div>
  </div>

  <div class="web">www.StrideDME.com</div>
</section>

<section class="card card--back">
  <div class="brand"><span class="brand__dot"></span>Stride DME</div>
  <div class="web">www.StrideDME.com</div>
</section>

</body>
</html>
```